Business card design needed

Hi we need a business card design for a new company based on the central coast NSW Australia
We do cakes for all occasions weddings, birthdays, christenings, engagement partys we also do cookie and cater for functions.
we would like to see the colours silver,black and a bright royal blue. (singapore orchid blue)

Industry/Entity Type

Royal

Contact Information for Business Card

Copperleaf Treats
Special occasions cake's and cookies
copperleaf.treats@mailbarrow.com
Rosalie Thwaite
48 Fernhill Street Walbarra
NSW 2274

```html
<!DOCTYPE html>
<html lang="en">
<head>
<meta charset="utf-8">
<title>Copperleaf Treats – Business Card</title>
<link rel="stylesheet" href="https://fonts.googleapis.com/css2?family=Parisienne&family=Crimson+Pro:wght@400&display=swap">
<style>
  :root {
    --page: #efebe6;
    --orchid-blue: #2889b3;
    --sky-band: #47c3f0;
    --silver: #c4c4c4;
    --lace: #ffffff;
    --ink-white: #ffffff;
    --ink-dark: #111111;
  }
  html, body {
    margin: 0;
    width: 1200px;
    height: 1200px;
    overflow: hidden;
    background: var(--page);
  }
  .card {
    position: absolute;
    left: 60px;
    top: 265px;
    width: 1080px;
    height: 670px;
    overflow: hidden;
    background: var(--orchid-blue);
    box-shadow: 0 4px 12px rgba(0,0,0,0.25);
  }
  .card-shapes {
    position: absolute;
    inset: 0;
  }
  .brand-name {
    position: absolute;
    left: 424px;
    top: 270px;
    transform: translateX(-50%);
    margin: 0;
    font-family: "Parisienne", cursive;
    font-weight: 400;
    font-size: 70px;
    line-height: 72px;
    color: var(--ink-white);
    text-align: center;
    white-space: nowrap;
  }
  .tagline {
    position: absolute;
    left: 424px;
    top: 472px;
    transform: translateX(-50%);
    margin: 0;
    font-family: "Crimson Pro", serif;
    font-size: 30px;
    line-height: 42px;
    color: var(--ink-dark);
    text-align: center;
    white-space: nowrap;
  }
  .contact {
    position: absolute;
    right: 14px;
    top: 548px;
    text-align: right;
    color: var(--ink-dark);
  }
  .contact-name {
    margin: 0 0 2px;
    font-family: "Parisienne", cursive;
    font-size: 38px;
    line-height: 44px;
    color: var(--ink-white);
  }
  .contact-line {
    margin: 0;
    font-family: "Crimson Pro", serif;
    font-size: 24px;
    line-height: 28px;
  }
</style>
</head>
<body>
  <section class="card">
    <svg class="card-shapes" width="1080" height="670" viewBox="0 0 1080 670">
      <rect class="bottom-band" x="0" y="538" width="1080" height="132" fill="var(--sky-band)"/>
      <circle class="lace-doily" cx="424" cy="345" r="390" fill="var(--lace)" role="img" aria-label="White lace doily pattern"/>
      <circle class="silver-disc" cx="424" cy="353" r="362" fill="var(--silver)"/>
      <rect class="cupcake-silhouette" x="200" y="40" width="464" height="590" rx="180" fill="var(--orchid-blue)" role="img" aria-label="Blue cupcake silhouette illustration"/>
    </svg>

    <h1 class="brand-name">Copperleaf<br>Treats</h1>
    <p class="tagline">Special occasions<br>cakes and cookies</p>

    <div class="contact">
      <p class="contact-name">Rosalie Thwaite</p>
      <p class="contact-line">copperleaf.treats@mailbarrow.com</p>
      <p class="contact-line">48 Fernhill Street Walbarra NSW 2274</p>
    </div>
  </section>
</body>
</html>
```